Amber Ridge LLC Business Cards and Stationary
Amber Ridge LLC
Simple
Marcus Delford
C.E.O.
42 Tamarind Ct Stanton, CA, 90712
Marcus@amberridgeLLC.com
www.amberridgellc.com www.amberridgeproperty.com
I would like the front to be very clean, maybe only the logo, and maybe management and Real Estate Services
On the back of the card i would like all the information to leave a clean and organized look. Instead of Using Fax: written out i would prefer F:

```html
<!DOCTYPE html>
<html lang="en">
<head>
<meta charset="utf-8">
<title>Amber Ridge LLC — Business Card</title>
<link href="https://fonts.googleapis.com/css2?family=Montserrat:wght@400;500&display=swap" rel="stylesheet">
<style>
  :root {
    --page-bg: #e7e8ec;
    --card-white: #f6f7f9;
    --blue-light: #3d4cc2;
    --blue-deep: #262c92;
    --silver-light: #eef0f3;
    --silver-dark: #9ea3ab;
    --logo-grey: #8b9097;
    --tagline-grey: #a2a7ad;
    --accent-teal: #2d8fa8;
    --ink-white: #ffffff;
  }
  * { margin: 0; padding: 0; box-sizing: border-box; }
  html, body {
    width: 1200px; height: 768px; overflow: hidden;
    background: var(--page-bg);
    font-family: "Montserrat", Arial, sans-serif;
  }
  .card {
    position: absolute; left: 120px; top: 110px;
    width: 960px; height: 548px;
    background: var(--card-white);
    border-radius: 14px; overflow: hidden;
    box-shadow: 0 10px 30px rgba(0,0,0,.18);
  }
  .card-shapes { position: absolute; inset: 0; }
  .brand {
    position: absolute; left: 40px; top: 190px; width: 460px;
    text-align: center;
  }
  .brand-row { display: flex; align-items: center; justify-content: center; gap: 14px; }
  .brand-dot { width: 22px; height: 22px; border-radius: 50%; background: var(--accent-teal); }
  .brand-name {
    font-weight: 400; font-size: 36px; letter-spacing: 2px;
    color: var(--logo-grey); text-transform: uppercase;
  }
  .brand-tagline {
    margin-top: 14px; font-size: 19px; letter-spacing: 5px;
    color: var(--tagline-grey); text-transform: uppercase;
  }
  .contact {
    position: absolute; left: 610px; top: 108px; width: 320px;
    color: var(--ink-white);
  }
  .person-name { font-size: 25px; font-weight: 500; }
  .person-role { font-size: 19px; margin-top: 4px; }
  .address { margin-top: 82px; font-size: 17px; line-height: 26px; }
  .details { margin-top: 40px; list-style: none; font-size: 15px; }
  .details li { display: flex; align-items: center; gap: 10px; height: 25px; }
  .details svg { width: 14px; height: 14px; flex: none; }
</style>
</head>
<body>
  <div class="card">
    <svg class="card-shapes" viewBox="0 0 960 548" width="960" height="548" aria-hidden="true">
      <defs>
        <linearGradient id="panelBlue" x1="0" y1="0" x2="1" y2="1">
          <stop offset="0" stop-color="var(--blue-light)"/>
          <stop offset="1" stop-color="var(--blue-deep)"/>
        </linearGradient>
        <linearGradient id="silverBand" x1="0" y1="0" x2="1" y2="0">
          <stop offset="0" stop-color="var(--silver-light)"/>
          <stop offset="1" stop-color="var(--silver-dark)"/>
        </linearGradient>
      </defs>
      <path d="M515 0 C455 150 450 380 495 548 L540 548 C498 380 505 150 565 0 Z" fill="url(#silverBand)"/>
      <path d="M575 0 C512 150 506 380 548 548 L960 548 L960 0 Z" fill="url(#panelBlue)"/>
      <path d="M565 0 C505 150 498 380 540 548" fill="none" stroke="#ffffff" stroke-width="3"/>
    </svg>

    <div class="brand">
      <div class="brand-row">
        <span class="brand-dot"></span>
        <span class="brand-name">Amber Ridge LLC</span>
      </div>
      <div class="brand-tagline">Management Services</div>
    </div>

    <div class="contact">
      <div class="person-name">Dana Orlow</div>
      <div class="person-role">consultant</div>
      <div class="address">27 Linden Row Mall<br>Harbor Road LAD</div>
      <ul class="details">
        <li><svg viewBox="0 0 16 16"><rect x="4" y="1" width="8" height="14" rx="1.5" fill="none" stroke="#fff" stroke-width="1.5"/><circle cx="8" cy="12.5" r="1" fill="#fff"/></svg>555 210 4417</li>
        <li><svg viewBox="0 0 16 16"><path d="M3 2 L6 2 L7 5 L5.5 6.5 C6.5 8.5 7.5 9.5 9.5 10.5 L11 9 L14 10 L14 13 C8 14 2 8 3 2 Z" fill="#fff"/></svg>555 210 4417</li>
        <li><svg viewBox="0 0 16 16"><rect x="1.5" y="5" width="13" height="8" rx="1" fill="none" stroke="#fff" stroke-width="1.5"/><rect x="4" y="2" width="8" height="3" fill="#fff"/></svg>555 210 4417</li>
        <li><svg viewBox="0 0 16 16"><rect x="1.5" y="3.5" width="13" height="9" rx="1" fill="none" stroke="#fff" stroke-width="1.5"/><path d="M2 4 L8 9 L14 4" fill="none" stroke="#fff" stroke-width="1.5"/></svg>info@amberridgellc.com</li>
        <li><svg viewBox="0 0 16 16"><circle cx="8" cy="8" r="6.5" fill="none" stroke="#fff" stroke-width="1.5"/><path d="M1.5 8 H14.5 M8 1.5 C5 5 5 11 8 14.5 M8 1.5 C11 5 11 11 8 14.5" fill="none" stroke="#fff" stroke-width="1.2"/></svg>www.amberridgellc.com</li>
      </ul>
    </div>
  </div>
</body>
</html>
```